An anniversary gift for my girlfriend

My girlfriend and I have been dating for almost 2 years. We met online and this has afforded us the really unique opportunity to have the first words we said to each other (the whole conversation, in fact) preserved. We're moving in together in a few months and she doesn't know that I saved the conversation. I've been waiting for this to turn it into something we can hang in our new place.

The only phrase I want to use is:
"Well if you dislike people's knees then I think we'll get along famously"

It's an Nobody Leaves Before Midnight in Portland reference for the curious.

I want the poster to use the words themselves as the art; I'm thinking typography. I'd like it to match her aesthetic, she likes to wear Nora Vell and T. Brisk. Colors shouldn't be anything too "girly". Somewhere I'd like to include the date June 1, 2015. It shouldn't be a major piece of the poster though, just a way to denote the date.

It should fit (and be fully visible in) a 16x20 (inches) frame

Thanks in advance for the work!

Requirements
Must have
• Must use only the words: "Well if you dislike people's knees then I think we'll get along famously"
• I want this to be typography, so making the phrase the center of the poster and the art itself.

```html
<!DOCTYPE html>
<html lang="en">
<head>
<meta charset="utf-8">
<title>Well If You Dislike People's Knees</title>
<link rel="stylesheet" href="https://fonts.googleapis.com/css2?family=Oswald:wght@700&display=swap">
<style>
  :root {
    --poster-bg: #b86055;
    --heart-fill: #df6b5c;
    --type-colour: #dcab9f;
  }
  html, body {
    margin: 0;
    padding: 0;
    width: 960px;
    height: 1200px;
    overflow: hidden;
    background: var(--poster-bg);
  }
  .poster {
    position: relative;
    width: 960px;
    height: 1200px;
    background: var(--poster-bg);
  }
  .poster__art,
  .poster__quote {
    position: absolute;
    left: 0;
    top: 0;
    width: 960px;
    height: 1200px;
  }
  .poster__heart {
    fill: var(--heart-fill);
  }
  .quote-line {
    font-family: 'Oswald', 'Arial Narrow', sans-serif;
    font-weight: 700;
    fill: var(--type-colour);
    text-transform: uppercase;
  }
</style>
</head>
<body>
  <main class="poster">
    <svg class="poster__art" viewBox="0 0 960 1200" role="img"
         aria-label="Illustration of a couple's legs, her in heels and him in dark trousers, stepping together in front of a large heart">
      <path class="poster__heart"
            d="M479 140 C430 40 194 0 194 230 C194 380 380 460 479 550 C578 460 764 380 764 230 C764 0 528 40 479 140 Z"/>
    </svg>

    <svg class="poster__quote" viewBox="0 0 960 1200">
      <text class="quote-line quote-line--well" x="193" y="704" font-size="155" textLength="328" lengthAdjust="spacingAndGlyphs">Well</text>
      <text class="quote-line" x="533" y="642" font-size="73" textLength="246" lengthAdjust="spacingAndGlyphs">If you</text>
      <text class="quote-line" x="533" y="704" font-size="72" textLength="246" lengthAdjust="spacingAndGlyphs">Dislike</text>
      <text class="quote-line" x="193" y="800" font-size="103" textLength="586" lengthAdjust="spacingAndGlyphs">People’s knees</text>
      <text class="quote-line" x="193" y="900" font-size="110" textLength="586" lengthAdjust="spacingAndGlyphs">Then I think</text>
      <text class="quote-line quote-line--vertical" x="0" y="0" font-size="71" textLength="213" lengthAdjust="spacingAndGlyphs"
            transform="translate(250 1117) rotate(-90)">We’ll</text>
      <text class="quote-line" x="258" y="1004" font-size="120" textLength="521" lengthAdjust="spacingAndGlyphs">Get along</text>
      <text class="quote-line" x="258" y="1117" font-size="130" textLength="521" lengthAdjust="spacingAndGlyphs">Famously</text>
    </svg>
  </main>
</body>
</html>
```